LAW FIRM - RE-DESIGN - (professional, excellence, tradition and innovation)

We are a premier law firm in New South Wales, Australia. We pride ourselves on being cutting edge and up to date in our market.

Our firm formed in 1874 and has a particularly strong tradition within it's geographic footprint. acting for clients over multiple generations. Despite our regional background, our reputation for excellence has enable us to remain highly visible in a large area.

We have invested heavily in ensuring future planning of this business, and do so on a recurring basis. This has lead to a review of our existing web site.

Although serviceable we feel our previous website is out-of-date and not as in touch with the modern market. We are aware that for the emerging clients a web site is often the face of a firm and a failure to hold attention on the first page may fail to capture the client.

We are seeking designs to communicate the core values of professionalism and excellence. At the same time as maintaining traditional country values of honesty, integrity and hard work we strive to embrace changes to the law and technology.

Target Market(s)

Clients of Law Firm

Industry/Entity Type

Law Firm

Coding

Coded - Design and coding required

Number of Pages Required

5+ page

Requirements
Must have
• A strong sense of professionalism and excellence with a careful balance between traditional values and innovation.
Nice to have
• We have included within our design brief links to top competitors sites to assist for design concepts.

```html
<!DOCTYPE html>
<html lang="en">
<head>
<meta charset="utf-8">
<title>Harlow Law</title>
<link href="https://fonts.googleapis.com/css2?family=Cinzel:wght@400;600&family=Noto+Serif&family=Open+Sans:wght@400;600&family=Poppins:wght@400;500;600&display=swap" rel="stylesheet">
<style>
:root{
  --navy:#0e3a73;
  --blue:#1450a0;
  --gold:#c8a83d;
  --ink:#333;
  --muted:#777;
  --line:#e4e4e4;
  --footer:#262626;
  --footer-base:#1c1c1c;
  --footer-text:#9a9a9a;
  --cta:#1d63d6;
  --white:#fff;
}
*{margin:0;padding:0;box-sizing:border-box}
html,body{width:1200px;height:2769px;overflow:hidden}
body{position:relative;background:var(--white);font-family:"Open Sans",sans-serif;color:var(--ink)}
.abs{position:absolute}

/* Header */
.site-header{left:0;top:0;width:1200px;height:122px;background:var(--white)}
.brand{left:79px;top:44px;display:flex;align-items:center;gap:10px;font-family:"Cinzel",serif;font-weight:600;font-size:28px;color:var(--navy);letter-spacing:.5px;white-space:nowrap}
.brand-dot{width:18px;height:18px;background:var(--navy)}
.main-nav{left:353px;top:68px;display:flex;gap:29px;font-family:"Poppins",sans-serif;font-weight:500;font-size:14px;color:var(--navy);white-space:nowrap}
.main-nav .active{color:var(--gold)}
.btn-consult{left:938px;top:57px;width:173px;height:41px;background:var(--gold);color:var(--white);font-family:"Poppins",sans-serif;font-weight:500;font-size:15px;display:flex;align-items:center;justify-content:center}

/* Hero */
.hero{left:0;top:122px;width:1200px;height:635px;background:linear-gradient(135deg,#6b4a30 0%,#8a6444 35%,#a07a55 60%,#6e4e33 100%)}
.hero-title{left:0;top:316px;width:1120px;text-align:center;font-family:"Cinzel",serif;font-weight:400;font-size:29px;color:var(--white);letter-spacing:.3px;white-space:nowrap}
.hero-sub{left:0;top:372px;width:1120px;text-align:center;font-family:"Poppins",sans-serif;font-size:19px;color:var(--white)}
.btn-gold{left:489px;top:432px;width:152px;height:44px;background:var(--gold);color:#222;font-family:"Poppins",sans-serif;font-weight:500;font-size:15px;display:flex;align-items:center;justify-content:center}

/* Feature boxes */
.features{left:80px;top:630px;width:1040px;height:223px;display:flex}
.feature{flex:1;background:var(--navy);color:var(--white);text-align:center;padding-top:22px}
.feature.mid{background:var(--blue)}
.feature svg{display:block;margin:0 auto}
.feature h3{font-family:"Cinzel",serif;font-weight:400;font-size:24px;letter-spacing:1px;margin-top:14px}
.feature p{font-size:13px;line-height:22px;margin:12px auto 0;width:290px;color:#dfe7f3}

/* About */
.about-title{left:79px;top:945px;font-family:"Cinzel",serif;font-weight:400;font-size:40px;color:var(--navy);letter-spacing:1px}
.about-lead{left:80px;top:1008px;width:500px;font-family:"Open Sans",sans-serif;font-weight:600;font-size:13.5px;line-height:24px;color:#333}
.about-body{left:80px;top:1072px;width:490px;font-size:12.6px;line-height:22px;color:#555}
.about-body p{margin-bottom:22px}
.about-photo{left:592px;top:905px;width:538px;height:517px;background:linear-gradient(180deg,#f4f4f4 0%,#cfcfcf 40%,#2a2a2e 70%,#151518 100%)}

/* Banner */
.banner{left:0;top:1422px;width:1200px;height:312px;background:linear-gradient(90deg,#3a2d23 0%,#6c5644 35%,#4b3b2f 70%,#2a211b 100%)}
.banner-title{left:400px;top:1500px;width:716px;text-align:center;font-family:"Cinzel",serif;font-weight:400;font-size:27px;color:var(--white);white-space:nowrap}
.banner-text{left:421px;top:1556px;width:674px;text-align:center;font-size:13.5px;line-height:23px;color:#eee}
.btn-navy{left:676px;top:1632px;width:166px;height:50px;background:var(--navy);color:var(--white);font-family:"Poppins",sans-serif;font-weight:600;font-size:14px;display:flex;align-items:center;justify-content:center}

/* People */
.people-title{left:0;top:1805px;width:1200px;text-align:center;font-family:"Cinzel",serif;font-weight:400;font-size:40px;color:var(--navy);letter-spacing:1px}
.person-card{top:2136px;width:227px;height:199px;border:1px solid var(--line);background:var(--white);text-align:center;padding-top:36px}
.person-card h4{font-family:"Noto Serif",serif;font-weight:400;font-size:17px;color:#333}
.person-card .role{font-size:11.5px;color:#999;margin-top:6px}
.person-social{display:flex;justify-content:center;gap:10px;margin-top:20px}
.person-social span{width:24px;height:24px;border-radius:50%;background:#eee}
.btn-bio{display:inline-flex;margin-top:18px;width:110px;height:32px;background:#1d1d1d;color:var(--white);font-family:"Poppins",sans-serif;font-size:11.5px;align-items:center;justify-content:center}
.person-photo{top:1933px;width:166px;height:166px;border-radius:50%;border:6px solid #ececec;background:linear-gradient(180deg,#e9e9e9,#b9b9b9)}
.c1{left:81px}.c2{left:351px}.c3{left:622px}.c4{left:893px}
.p1{left:111px}.p2{left:382px}.p3{left:654px}.p4{left:923px}

/* Footer */
.site-footer{left:0;top:2391px;width:1200px;height:341px;background:var(--footer)}
.footer-base{left:0;top:2732px;width:1200px;height:37px;background:var(--footer-base)}
.footer-brand{left:83px;top:2492px;display:flex;align-items:center;gap:10px;font-family:"Cinzel",serif;font-weight:600;font-size:28px;color:#bdbdbd;white-space:nowrap}
.footer-brand .brand-dot{background:#bdbdbd}
.footer-social{left:83px;top:2618px;display:flex;gap:9px}
.footer-social span{width:29px;height:29px;border-radius:50%;background:#555}
.footer-col h5{font-family:"Poppins",sans-serif;font-weight:600;font-size:14px;color:var(--white);letter-spacing:.3px}
.contact-list{list-style:none;margin-top:30px}
.contact-list li{display:flex;gap:12px;font-family:"Poppins",sans-serif;font-size:11.5px;line-height:24px;color:#bbb;margin-bottom:8px}
.contact-list svg{flex:none;margin-top:6px}
.info-list{list-style:none;margin-top:34px}
.info-list li{font-family:"Poppins",sans-serif;font-size:11px;color:#aaa;height:33px}
.info-list li::before{content:"›";color:#777;margin-right:12px}
.news-text{font-family:"Poppins",sans-serif;font-size:12.5px;line-height:27px;color:#8c8c8c;margin-top:24px;width:240px}
.news-input{margin-top:14px;width:238px;height:43px;border:1px solid #4a4a4a;color:#aaa;font-family:"Poppins",sans-serif;font-size:12.5px;padding:12px 18px}
.news-btn{margin-top:20px;width:238px;height:43px;background:var(--cta);color:var(--white);font-family:"Poppins",sans-serif;font-weight:500;font-size:13px;display:flex;align-items:center;justify-content:center}
</style>
</head>
<body>

<header class="abs site-header">
  <div class="abs brand"><span class="brand-dot"></span>Harlow Law</div>
  <nav class="abs main-nav">
    <span class="active">HOME</span><span>ABOUT US</span><span>SERVICES</span><span>OUR PEOPLE</span><span>FAQ</span><span>CONTACT US</span>
  </nav>
  <div class="abs btn-consult">Free Consultation</div>
</header>

<section class="abs hero" role="img" aria-label="Law books stacked on a wooden desk beside a judge's gavel"></section>
<h1 class="abs hero-title">HARLOW LAW HAS BEEN IN EXISTENCE SINCE 1874</h1>
<p class="abs hero-sub">Your Legal Solution Start Here!</p>
<div class="abs btn-gold">Read More</div>

<section class="abs features">
  <div class="feature">
    <svg width="64" height="64" viewBox="0 0 64 64" fill="none" stroke="#fff" stroke-width="3">
      <circle cx="24" cy="24" r="12"/><circle cx="24" cy="24" r="5"/>
      <path d="M24 6v6M24 36v6M6 24h6M36 24h6M11 11l4 4M33 33l4 4M11 37l4-4M33 15l4-4"/>
      <circle cx="46" cy="46" r="8"/><circle cx="46" cy="46" r="3"/>
      <path d="M46 34v4M46 54v4M34 46h4M54 46h4"/>
    </svg>
    <h3>OUR SERVICES</h3>
    <p>Claritas est etiam protcessus dynamicus, qui sequitur mutationem consuetudine</p>
  </div>
  <div class="feature mid">
    <svg width="64" height="64" viewBox="0 0 64 64" fill="#fff">
      <circle cx="22" cy="20" r="9"/><path d="M6 50c0-12 8-18 16-18s16 6 16 18z"/>
      <circle cx="44" cy="24" r="8"/><path d="M32 52c2-10 7-15 12-15s12 5 14 15z"/>
    </svg>
    <h3>OUR PEOPLE</h3>
    <p>Claritas est etiam protcessus dynamicus, qui sequitur mutationem consuetudine</p>
  </div>
  <div class="feature">
    <svg width="64" height="64" viewBox="0 0 64 64" fill="none" stroke="#fff" stroke-width="2.5">
      <path d="M32 8L12 22l8 24h24l8-24zM32 8v20M12 22l20 6 20-6M20 46l12-18 12 18"/>
      <g fill="#fff"><circle cx="32" cy="8" r="4"/><circle cx="12" cy="22" r="4"/><circle cx="52" cy="22" r="4"/><circle cx="20" cy="46" r="4"/><circle cx="44" cy="46" r="4"/><circle cx="32" cy="30" r="6"/></g>
      <path d="M24 58c0-6 4-9 8-9s8 3 8 9"/>
    </svg>
    <h3>COMMUNITY</h3>
    <p>Claritas est etiam protcessus dynamicus, qui sequitur mutationem consuetudine</p>
  </div>
</section>

<h2 class="abs about-title">ABOUT US</h2>
<p class="abs about-lead">Harlow Law (formerly known as Harlow Pryce &amp; Lennox) has been part of the New England Region of New South Wales for over a century.</p>
<div class="abs about-body">
  <p>Harlow Law has been in existence since 1874 originally starting out as the firm Walter Greaves of Glen Innes. In 1894 Walter Greaves was acquired by Colonel RT Harlow. The firm became known as EM Harlow &amp; Co. until early 1970 when it became Harlow &amp; Co, Harlow Pryce &amp; Co in 1979 and Harlow Pryce &amp; Lennox in 1982.</p>
  <p>Harlow Law is proud of its long and distinguished history as a regional law firm and its service to the region.</p>
  <p>In December 1999, the firm opened an office in Inverell taking over the practice of JL Marsh &amp; Associates. This was followed by the incorporation of Redfern &amp; Co in December 2000 and the Armidale office moved to larger premises in Faulkner Street.</p>
</div>
<div class="abs about-photo" role="img" aria-label="Barrister in black gown and white bands holding a red book"></div>

<section class="abs banner" role="img" aria-label="Scales of justice in a softly lit courtroom"></section>
<h2 class="abs banner-title">HARLOW LAW HAS BEEN IN EXISTENCE SINCE 1874</h2>
<p class="abs banner-text">Walter Greaves was acquired by Colonel RT Harlow. The firm became known as EM Harlow &amp; Co. until early 1970 when it became Harlow &amp; Co, Harlow Pryce &amp; Co in 1979 and Harlow Pryce &amp; Lennox in 1982.</p>
<div class="abs btn-navy">CONSULT NOW!</div>

<h2 class="abs people-title">OUR PEOPLE</h2>

<div class="abs person-card c1"><h4>Daniel Whitcombe</h4><div class="role">Founder and Manager</div><div class="person-social"><span></span><span></span><span></span></div><span class="btn-bio">Read Full Bio</span></div>
<div class="abs person-card c2"><h4>Tomas Okafor</h4><div class="role">Partner</div><div class="person-social"><span></span><span></span><span></span></div><span class="btn-bio">Read Full Bio</span></div>
<div class="abs person-card c3"><h4>Clara Benning</h4><div class="role">Counsel</div><div class="person-social"><span></span><span></span><span></span></div><span class="btn-bio">Read Full Bio</span></div>
<div class="abs person-card c4"><h4>Nadia Rowe</h4><div class="role">Associate</div><div class="person-social"><span></span><span></span><span></span></div><span class="btn-bio">Read Full Bio</span></div>

<div class="abs person-photo p1" role="img" aria-label="Portrait of the founder and manager"></div>
<div class="abs person-photo p2" role="img" aria-label="Portrait of the partner"></div>
<div class="abs person-photo p3" role="img" aria-label="Portrait of the counsel"></div>
<div class="abs person-photo p4" role="img" aria-label="Portrait of the associate"></div>

<footer class="abs site-footer"></footer>
<div class="abs footer-base"></div>
<div class="abs footer-brand"><span class="brand-dot"></span>Harlow Law</div>
<div class="abs footer-social"><span></span><span></span><span></span><span></span></div>

<div class="abs footer-col" style="left:351px;top:2425px;width:230px">
  <h5>GET IN TOUCH</h5>
  <ul class="contact-list">
    <li><svg width="10" height="13" viewBox="0 0 10 13"><path d="M5 0a5 5 0 0 0-5 5c0 4 5 8 5 8s5-4 5-8a5 5 0 0 0-5-5z" fill="#1d63d6"/><circle cx="5" cy="5" r="2" fill="#262626"/></svg>88 Elm Row, Northvale, NSW 2370, Australia</li>
    <li><svg width="12" height="12" viewBox="0 0 12 12"><path d="M2 0l3 3-1.5 2a7 7 0 0 0 3.5 3.5L9 7l3 3-2 2C5 12 0 7 0 2z" fill="#1d63d6"/></svg>(02) 5550 1874</li>
    <li><svg width="12" height="12" viewBox="0 0 12 12"><path d="M0 5l12-5-4 12-2-5z" fill="#1d63d6"/></svg>hello@harlowlaw.example</li>
    <li><svg width="9" height="13" viewBox="0 0 9 13"><rect x="1" y="1" width="7" height="11" rx="1" fill="none" stroke="#1d63d6" stroke-width="1.6"/></svg>(02) 5550 1874</li>
    <li><svg width="12" height="12" viewBox="0 0 12 12"><circle cx="6" cy="6" r="5" fill="none" stroke="#1d63d6" stroke-width="1.6"/><path d="M6 3v3h2" stroke="#1d63d6" stroke-width="1.4" fill="none"/></svg>Mon - Sat: 9:00 - 18:00</li>
  </ul>
</div>

<div class="abs footer-col" style="left:617px;top:2425px;width:230px">
  <h5>INFORMATION</h5>
  <ul class="info-list">
    <li>HOME</li><li>WHY HARLOW</li><li>COMMUNITY PROFILE</li><li>SUCCESS STORIES</li><li>EVENTS</li><li>CONTACT</li>
  </ul>
</div>

<div class="abs footer-col" style="left:884px;top:2425px;width:250px">
  <h5>NEWS LETTER</h5>
  <p class="news-text">Enter your email address for our mailing list to keep your self our lastest updated.</p>
  <div class="news-input">Email</div>
  <div class="news-btn">Sign up</div>
</div>

</body>
</html>
```